I need a website design for a unique tropical home in the Whitsundays. It is called the Korimba Grove and would like an African Baobab tree as a logo. It is an eco retreat on the ocean/beach with a large award winning house. Is suited to special celebrations, boutique weddings, Executive retreats. Have many wonderful photographs to be added. Should allow for contact to arrange a booking and if possible have a pricing and bookings calendar. Can look at Velutro.com.au as example.
Home page should have picture of house from air and description of the special uses as mentioned above. Can then go to next level for descriptions of rooms, features, attractions, rates, booking calendar and contact details.

```html
<!DOCTYPE html>
<html lang="en">
<head>
<meta charset="utf-8">
<title>Korimba Grove – Eco Retreat on the Ocean</title>
<link href="https://fonts.googleapis.com/css2?family=Open+Sans:ital,wght@0,400;0,600;1,400&display=swap" rel="stylesheet">
<style>
:root{
  --brown:#7a4a34;
  --green:#2f8a1f;
  --green-bright:#1fb51a;
  --text:#555;
  --grey-bg:#ededed;
  --footer:#333;
  --cal-head:#444;
  --cal-cell:#e6e6e6;
  --cal-mute:#f1f1f1;
  --highlight:#5fa9c4;
  --red:#c0282a;
}
*{margin:0;padding:0;box-sizing:border-box}
html,body{width:931px;height:1200px;overflow:hidden;background:#fff}
body{font-family:"Open Sans",sans-serif;color:var(--text);position:relative}
.abs{position:absolute}
.brand-mark{left:78px;top:8px;width:59px;height:81px;background:var(--green)}
.brand-name{left:146px;top:26px;font-size:34px;color:var(--brown);font-weight:400;letter-spacing:.5px}
.contact{right:78px;top:14px;text-align:right;color:#777;font-size:13px;line-height:19.5px}
.contact h2{font-size:16px;font-weight:600;color:var(--brown);margin-bottom:8px}
.contact span{color:var(--green)}
.nav{left:0;top:106px;width:931px;height:37px;background:linear-gradient(#8b5a43,#6a3c29)}
.nav .active{position:absolute;left:77px;top:0;width:96px;height:37px;background:linear-gradient(#a9775e,#8a5a43)}
.nav a{position:absolute;top:11px;color:#fff;font-size:11.5px;text-decoration:none;transform:translateX(-50%)}
.hero{left:0;top:143px;width:931px;height:386px;background:linear-gradient(180deg,#4a7042 0%,#4d7a5c 55%,#3f8d9e 100%)}
.caption{left:79px;top:440px;width:396px;height:72px;background:#fff;border-left:6px solid var(--green-bright);padding:10px 0 0 15px}
.caption h1{font-size:19.5px;font-weight:400;color:var(--green);line-height:26px}
.caption p{font-size:11.5px;color:#6a2b10}
.slide-btn{top:486px;width:26px;height:26px;border-radius:50%;background:rgba(235,235,235,.8)}
h2.section{font-weight:400;color:var(--green)}
.welcome-title{left:79px;top:546px;font-size:18px}
.welcome-text{left:79px;top:579px;width:573px;font-size:10.5px;line-height:17.8px}
.divider{left:78px;top:688px;width:573px;height:1px;background:#ddd}
.rooms-title{left:79px;top:703px;font-size:14.6px}
.room{width:180px;height:99px}
.calendar{left:669px;top:552px;width:184px}
.cal-head{height:31px;background:var(--cal-head);color:#fff;font-size:12px;display:flex;align-items:center;justify-content:space-between;padding:0 9px}
.cal-head b{font-weight:600}
.cal-days,.cal-grid{display:grid;grid-template-columns:repeat(7,1fr);gap:1px}
.cal-days{font-size:7.5px;text-align:center;padding:5px 0 3px;color:#555}
.cal-grid div{height:25.5px;background:var(--cal-cell);font-size:10.5px;font-weight:600;display:flex;align-items:center;justify-content:center;color:#555}
.cal-grid .mute{background:var(--cal-mute);color:#aaa;font-weight:400}
.cal-grid .today{background:var(--highlight);color:#fff}
.cal-grid .event{color:var(--red)}
.features{left:669px;top:745px;width:184px;height:204px;background:linear-gradient(#3a9a2a,#217516)}
.features h2{font-size:19.5px;font-weight:400;color:#fff;text-align:center;padding-top:11px;height:45px;border-bottom:1px solid rgba(255,255,255,.15)}
.features ul{list-style:none;padding:9px 0 0 15px}
.features li{color:#fff;font-size:12px;height:27.5px;display:flex;align-items:center;gap:7px}
.testimonials{left:0;top:976px;width:931px;height:144px;background:var(--grey-bg)}
.testimonials h2{position:absolute;top:16px;width:100%;text-align:center;font-size:15px;font-weight:400;color:var(--green)}
.avatar{left:125px;top:45px;width:66px;height:78px;background:#fff;border:1px solid #ddd}
.avatar .photo{position:absolute;left:4px;top:4px;width:56px;height:57px;background:linear-gradient(#6b6f7a,#2e3038)}
.avatar span{position:absolute;bottom:2px;width:100%;text-align:center;font-size:7.5px;color:#555}
.quote{left:223px;top:45px;width:583px;height:78px;background:#fff;border:1px solid #ddd;border-radius:3px;padding:9px 18px 0 24px;font-style:italic;font-size:11.5px;line-height:19.5px;color:#666}
.quote:before{content:"";position:absolute;left:-11px;top:28px;border:10px solid transparent;border-right-color:#fff;border-left:0}
.footer{left:0;top:1120px;width:931px;height:80px;background:var(--footer);color:#ccc;font-size:10.5px}
.footer nav{position:absolute;left:78px;top:18px}
.footer nav a{color:#ddd;text-decoration:none}
.footer nav i{font-style:normal;color:#777;margin:0 9px}
.footer p{position:absolute;left:78px;top:44px}
.social{top:30px;width:19px;height:19px;border-radius:3px}
</style>
</head>
<body>
<header>
  <div class="abs brand-mark"></div>
  <div class="abs brand-name">Korimba Grove</div>
  <div class="abs contact">
    <h2>Contact us</h2>
    Call us : <span>655 210 4837</span><br>
    E-mail : <span>info@korimbagrove.com</span>
  </div>
</header>

<nav class="abs nav">
  <div class="active"></div>
  <a href="#" style="left:124px">HOME</a>
  <a href="#" style="left:223px">ROOMS</a>
  <a href="#" style="left:334px">FEATURES</a>
  <a href="#" style="left:461px">ATTRACTIONS</a>
  <a href="#" style="left:577px">RATES</a>
  <a href="#" style="left:683px">BOOKING</a>
  <a href="#" style="left:797px">CONTACT</a>
</nav>

<section class="abs hero" role="img" aria-label="Aerial photograph of the retreat, bushland with houses above a sandy beach and turquoise ocean"></section>
<div class="abs caption">
  <h1>AN ECO RETREAT ON THE OCEAN</h1>
  <p>Suited to special celebrations, boutique weddings, Executive retreats</p>
</div>
<svg class="abs slide-btn" style="left:801px" viewBox="0 0 26 26"><path d="M15 8l-5 5 5 5" fill="none" stroke="#999" stroke-width="1.5"/></svg>
<svg class="abs slide-btn" style="left:828px" viewBox="0 0 26 26"><path d="M11 8l5 5-5 5" fill="none" stroke="#999" stroke-width="1.5"/></svg>

<h2 class="abs section welcome-title">WELCOME TO KORIMBA GROVE</h2>
<p class="abs welcome-text">Etiam vulputate lorem ante, quis cursus justo scelerisque nec. Cras aliquet lacinia nisl eu elementum. Morbi molestie ipsum odio, et porta nisl malesuada eget. Morbi dapibus imperdiet mi nec accumsan. Maecenas rhoncus quam nec facilisis facilisis. Duis tempus leo eu urna adipiscing, ac egestas turpis vehicula. Phasellus nisl dolor, cursus et dolor id, feugiat elementum erat. Aenean tortor diam, molestie vitae ligula sit amet, pellentesque consequat libero. Aenean aliquam congue est, id dapibus sem viverra vel.</p>
<div class="abs divider"></div>
<h2 class="abs section rooms-title">OUR ROOMS</h2>
<div class="abs room" style="left:79px;top:736px;background:linear-gradient(#c9b6a0,#8a5a3a)" role="img" aria-label="Living room with dining table and bookshelves"></div>
<div class="abs room" style="left:275px;top:736px;background:linear-gradient(#1e3a70,#2a2a1c 60%,#8a7a40)" role="img" aria-label="House lit up at night among trees"></div>
<div class="abs room" style="left:470px;top:736px;background:linear-gradient(#8a8a70,#9a6a4a)" role="img" aria-label="Covered veranda with cane chairs"></div>
<div class="abs room" style="left:79px;top:849px;background:linear-gradient(#eae6e0,#9a7a5a)" role="img" aria-label="Sitting area with daybed and blue cushions"></div>
<div class="abs room" style="left:275px;top:849px;background:linear-gradient(#e6dccc,#8a4a2a)" role="img" aria-label="Bedroom with four-poster bed and white netting"></div>
<div class="abs room" style="left:470px;top:849px;background:linear-gradient(#cfc9bd,#f2f0ec)" role="img" aria-label="Simple bedroom with white bed and window blinds"></div>

<aside class="abs calendar">
  <div class="cal-head"><span>◄</span><b>February 2014</b><span>►</span></div>
  <div class="cal-days"><span>MON</span><span>TUE</span><span>WED</span><span>THU</span><span>FRI</span><span>SAT</span><span>SUN</span></div>
  <div class="cal-grid">
    <div class="mute">28</div><div>1</div><div>2</div><div>3</div><div class="today">4</div><div>5</div><div>6</div>
    <div>7</div><div>8</div><div>9</div><div>10</div><div>11</div><div>12</div><div>13</div>
    <div>14</div><div>15</div><div>16</div><div>17</div><div class="event">18</div><div>19</div><div>20</div>
    <div>21</div><div class="event">22</div><div>23</div><div>24</div><div>25</div><div>26</div><div>27</div>
    <div>28</div><div>29</div><div>30</div><div>31</div><div class="mute">1</div><div class="mute">2</div><div class="mute">3</div>
  </div>
</aside>

<aside class="abs features">
  <h2>OUR FEATURES</h2>
  <ul>
    <li><svg width="9" height="8" viewBox="0 0 9 8"><path d="M1 4l2.5 2.5L8 1" fill="none" stroke="#fff" stroke-width="1.6"/></svg>All types of Bed Facilities</li>
    <li><svg width="9" height="8" viewBox="0 0 9 8"><path d="M1 4l2.5 2.5L8 1" fill="none" stroke="#fff" stroke-width="1.6"/></svg>Wi-fi Connections</li>
    <li><svg width="9" height="8" viewBox="0 0 9 8"><path d="M1 4l2.5 2.5L8 1" fill="none" stroke="#fff" stroke-width="1.6"/></svg>Swimming Pool</li>
    <li><svg width="9" height="8" viewBox="0 0 9 8"><path d="M1 4l2.5 2.5L8 1" fill="none" stroke="#fff" stroke-width="1.6"/></svg>Attached Bar Facilities</li>
    <li><svg width="9" height="8" viewBox="0 0 9 8"><path d="M1 4l2.5 2.5L8 1" fill="none" stroke="#fff" stroke-width="1.6"/></svg>Massage Center</li>
  </ul>
</aside>

<section class="abs testimonials">
  <h2>Testimonials</h2>
  <svg class="abs" style="left:78px;top:60px" width="18" height="24" viewBox="0 0 18 24"><path d="M14 3L5 12l9 9" fill="none" stroke="#bbb" stroke-width="4"/></svg>
  <div class="abs avatar"><div class="photo" role="img" aria-label="Guest portrait"></div><span>Marcus</span></div>
  <div class="abs quote">Nullam risus nisi, blandit a convallis nec, vehicula quis augue. Donec sed lobortis eros, at commodo magna. Fusce ullamcorper, purus ut imperdiet luctus, arcu felis accumsan nulla, ut mollis arcu lectus quis erat. Morbi enim turpis, sollicitudin vel elementum non, tempor ac velit. Phasellus quis orci ante.</div>
  <svg class="abs" style="left:836px;top:60px" width="18" height="24" viewBox="0 0 18 24"><path d="M4 3l9 9-9 9" fill="none" stroke="#bbb" stroke-width="4"/></svg>
</section>

<footer class="abs footer">
  <nav><a href="#">Home</a><i>|</i><a href="#">Rooms</a><i>|</i><a href="#">Features</a><i>|</i><a href="#">Attractions</a><i>|</i><a href="#">Rates</a><i>|</i><a href="#">Booking</a><i>|</i><a href="#">Contact</a></nav>
  <p>Copyright © 2014 Korimba Grove.&nbsp;&nbsp; All rights reserved.</p>
  <div class="abs social" style="left:810px;background:#3b5a9a"></div>
  <div class="abs social" style="left:834px;background:#3aa8dc"></div>
</footer>
</body>
</html>
```